Website for a financial survey consultancy

WHO WE ARE
We're a niche HR consultancy specialising in salary comparison surveys for the financial asset management industry. We position ourselves as a small, highly responsive organisation with a strong personal relationship with each of our 50+ blue-chip clients.

WHAT WE DO
Our business is 80% surveys (= products), 20% consultancy (= services). The surveys are a set of online products which clients interact with to find the information they are interested in.

WHAT WE WANT
We are completely revising our existing marketing website and need a new up-to-date look and feel for the site. We want you to design 2 web pages
- Home page
- Internal content page

More details below in Must Have Priorities.

REFERENCE SITES
- www.pellimorn.com - nice background image
- www.vantrikel.com - ignoring the animations
- www.quorvalen.com
- www.lumiscap.com - clean, fresh, styly but prob not corporate enough
- www.dorvethfunds.com - spacious, beautiful, slightly dated tho
- www.thalbin.co.uk - ignore the colours. Like the simplicity, larger font size (although want to stick with sans-serif fonts for main content)

DELIVERABLES
The final designs should be delivered as one or more PSD files with clearly named layers. All design elements and treatments should be separated out, for example use adjustment layers rather than applied (and subsequently irreversible) adjustments, strokes, shading, etc.

WHAT NEXT
I'll be monitoring the contest every day and can respond to questions fast. You can IM me on Skype or MSN.
Updates

Project Deadline Extended
Reason: Hi folks,

I am extending the deadline to this project as I am travelling this week and therefore will not be able to make a final decision until next Monday. I will try and provide further feedback over the course of this week but I am only going to be online occasionally so be prepared to wait a few days for a reply from me.

Thanks for all the designs so far.

Owen

Target Market(s)

In order of importance, most important first

1. Potential customers - UK & US financial industry HR professionals, short on time. Heard about us already, want to find out more about what we do, confirm relevance for their needs. Core goal - establish credibility: are we properly resourced, will we be around for years to come, are we *real*.

2. Existing customers - UK & US financial industry professionals, short on time, under pressure, want results quickly, minimum faff, expect high quality, slickly presented information. Primary action: login and use surveys.

3. Industry professionals/researchers - probably arriving through blog content, looking to browse and hoover information. Valuable for their ability to spread awareness of who we are amongst their peers.

Industry/Entity Type

Financial

Requirements
Must have
• GENERAL
Style cues - Corporate, professional, financial, stylish, slick, clean, spacious, light
Size - standard 960px grid

NAVIGATION
- [ Home | About us | Surveys | Consulting | Blog ]
- Sub-nav (roll-over dropdown) on About Us, Surveys & Consulting

ALL PAGES
- Site navigation
- Client login (on screen permanently or link to ajaxy in-page pop-up)
- Footer section
- Existing logo (attached)* - this is obviously an important reference point in the design, esp colour

HOME PAGE
- Communicate (link thru to?) survey/consulting split
- Large photo(s)/backdrop (2-3 interchangeable options ideally). Please consider what rights agreement will be necessary for any photos you include in your design.
- Possibly bigger more prominent version of logo
- Strap line/sentence - "Focussed data is the key to success"
- 3 recent blog posts (should look good with and without blog post images)
- Free downloadable PDF research report + supporting blurb

INTERNAL PAGE
- Page title
- Content - typical page will be less than one screenfull
- Level 1 sub-heading
- Level 2 sub-heading
- Bulleted list
- Content supporting image (any image will do - interested in placement, borders (if any), spacing, caption, etc)
- 'Do something' button

* Note: there is some internal debate about this logo at the moment. Some (me) are keen for it to change, some (not me!) are not. If you have an web page design idea/concept that requires an evolution of the logo, go ahead and evolve it. We can explore this further in the design process as necessary, but don't sweat it.
Nice to have
• Values to communicate
- Knowledgeable
- Professional
- Secure
- Personal
- Experienced
- Financial industry specific
- Accurate
- Reliable
Should not have
• - Search box
- Social media links, other than RSS feed button (discrete)

```html
<!DOCTYPE html>
<html lang="en">
<head>
<meta charset="utf-8">
<title>NVXi — Focussed data is the key to success</title>
<link rel="stylesheet" href="https://fonts.googleapis.com/css2?family=Alegreya+Sans:ital,wght@0,400;0,700;1,300;1,400;1,700&family=Tenor+Sans&family=Arimo:wght@400;700&family=Lato:ital,wght@1,300;1,400&display=swap">
<style>
  :root {
    --sky-light: #dfe8ec;
    --sky-mid: #a9c0cb;
    --panel-dark: rgba(28, 33, 36, 0.93);
    --panel-glass: rgba(30, 38, 42, 0.72);
    --blog-glass: rgba(8, 10, 12, 0.84);
    --ink-white: #ffffff;
    --ink-soft: #e6e9ea;
    --rule-soft: rgba(255, 255, 255, 0.28);
    --footer-black: #0b0b0b;
    --footer-grey: #8f8f8f;
    --pdf-red: #b3141a;
    --pdf-dark: #2b2b2b;
  }
  * { margin: 0; padding: 0; box-sizing: border-box; }
  html, body { width: 1200px; height: 640px; overflow: hidden; background: var(--footer-black); }
  .page { position: relative; width: 1200px; height: 640px; overflow: hidden; font-family: "Arimo", Arial, sans-serif; }

  .backdrop {
    position: absolute; left: 0; top: 0; width: 1200px; height: 616px;
    background:
      linear-gradient(115deg, transparent 55%, rgba(127,138,108,0.55) 78%, rgba(60,70,60,0.6) 100%),
      linear-gradient(128deg, transparent 28%, rgba(63,127,163,0.75) 40%, rgba(40,70,95,0.8) 52%, rgba(185,193,194,0.85) 62%, rgba(90,100,100,0.6) 74%, transparent 88%),
      linear-gradient(180deg, var(--sky-mid) 0%, var(--sky-light) 100%);
  }

  .brand-column {
    position: absolute; left: 103px; top: 0; width: 189px; height: 438px;
    background: var(--panel-dark);
  }
  .brand-name {
    position: absolute; left: 35px; top: 150px; width: 122px;
    font-family: "Tenor Sans", sans-serif; font-size: 44px; line-height: 52px; color: var(--ink-white);
  }

  .main-nav { position: absolute; left: 35px; top: 283px; width: 122px; list-style: none; }
  .main-nav li {
    height: 28.6px; line-height: 28px; border-bottom: 1px solid rgba(255,255,255,0.12);
    font-family: "Alegreya Sans", sans-serif; font-style: italic; font-weight: 300;
    font-size: 18px; color: var(--ink-soft); letter-spacing: 0.5px; white-space: nowrap;
  }
  .main-nav li:last-child { border-bottom: none; }
  .main-nav li.is-current { font-weight: 700; color: var(--ink-white); }

  .client-login {
    position: absolute; left: 1000px; top: 16px; width: 108px; height: 22px;
    background: #000; color: var(--ink-white); text-align: center;
    font-family: "Alegreya Sans", sans-serif; font-style: italic; font-weight: 700; font-size: 16px; line-height: 22px;
  }

  .strapline-panel {
    position: absolute; left: 103px; top: 461px; width: 591px; height: 128px;
    background: var(--panel-glass); padding: 6px 9px;
  }
  .strapline-panel h1 {
    font-family: "Tenor Sans", sans-serif; font-weight: 400; font-size: 30px; line-height: 38px; color: var(--ink-white);
    white-space: nowrap;
  }
  .strapline-panel p {
    margin-top: 4px; font-family: "Lato", sans-serif; font-style: italic; font-weight: 300;
    font-size: 15.5px; line-height: 17px; color: var(--ink-soft); white-space: nowrap;
  }

  .latest-blog {
    position: absolute; left: 815px; top: 267px; width: 293px; height: 249px;
    background: var(--blog-glass); padding: 10px 11px 0 11px;
  }
  .latest-blog h2 {
    font-family: "Alegreya Sans", sans-serif; font-weight: 700; font-size: 15px; letter-spacing: 1px;
    color: var(--ink-white); padding-bottom: 3px; border-bottom: 1px solid var(--ink-soft); word-spacing: 3px;
  }
  .blog-post { padding: 11px 3px 7px; border-bottom: 1px solid var(--rule-soft); }
  .blog-post:last-child { border-bottom: none; }
  .blog-post p { font-size: 11px; line-height: 17px; color: var(--ink-soft); }
  .blog-post time { display: block; font-size: 11px; line-height: 17px; font-weight: 700; color: var(--ink-white); text-decoration: underline; }

  .report-download {
    position: absolute; left: 814px; top: 541px; width: 266px; height: 47px; border-radius: 4px;
    background: linear-gradient(180deg, #ffffff 0%, #e8e8e8 100%); box-shadow: 0 1px 3px rgba(0,0,0,0.35);
  }
  .report-icon { position: absolute; left: 6px; top: 6px; width: 38px; height: 35px; background: var(--pdf-red); border-radius: 2px; }
  .report-title { position: absolute; left: 53px; top: 7px; font-family: "Lato", sans-serif; font-style: italic; font-weight: 300; font-size: 13.5px; color: var(--pdf-dark); white-space: nowrap; }
  .report-note { position: absolute; left: 53px; top: 25px; font-family: "Lato", sans-serif; font-style: italic; font-weight: 400; font-size: 11.5px; color: var(--pdf-red); white-space: nowrap; }

  .site-footer {
    position: absolute; left: 0; top: 616px; width: 1200px; height: 24px; background: var(--footer-black);
    font-size: 11.5px; line-height: 24px; color: var(--footer-grey); white-space: nowrap;
  }
  .footer-copy { position: absolute; left: 6px; }
  .footer-contact { position: absolute; left: 224px; color: var(--ink-white); word-spacing: 2px; }
  .footer-contact span { margin: 0 9px; }
  .footer-links { position: absolute; right: 7px; }
</style>
</head>
<body>
<div class="page">
  <div class="backdrop" role="img" aria-label="Photograph of a modern glass and stone office building against a pale blue sky"></div>

  <header class="brand-column">
    <div class="brand-name">NVXi</div>
    <ul class="main-nav">
      <li class="is-current">HOME</li>
      <li>ABOUT US</li>
      <li>SURVEYS</li>
      <li>CONSULTING</li>
      <li>BLOG</li>
    </ul>
  </header>

  <div class="client-login">Client login</div>

  <section class="strapline-panel">
    <h1>Focussed data is the key to success</h1>
    <p>It is a long established fact that a reader will be distracted by the readable<br>
    content of a page when looking at its layout. The point of using Lorem Ipsum<br>
    is that it has a more-or-less normal distribution of letters, as opposed to using<br>
    'Content here, content here', making it look like readable English</p>
  </section>

  <aside class="latest-blog">
    <h2>LATEST BLOG</h2>
    <article class="blog-post">
      <p>fact that a reader will be distracted by the readable fact that a reader will be distracted</p>
      <time>9:53 AM Fabruary 1, 2011</time>
    </article>
    <article class="blog-post">
      <p>fact that a reader will be distracted by the readable fact that a reader will be distracted</p>
      <time>9:53 AM Fabruary 1, 2011</time>
    </article>
    <article class="blog-post">
      <p>fact that a reader will be distracted by the readable fact that a reader will be distracted</p>
      <time>9:53 AM Fabruary 1, 2011</time>
    </article>
  </aside>

  <div class="report-download">
    <div class="report-icon"></div>
    <div class="report-title">Research report + supporting blurb</div>
    <div class="report-note">Free downloadable PDF</div>
  </div>

  <footer class="site-footer">
    <span class="footer-copy">© 2011 NVXi, Inc. All rights reserved.</span>
    <span class="footer-contact">Phone: 0000-1234-1234<span>|</span>info@nvxi.com</span>
    <span class="footer-links">Terms and Conditions | Privacy Policy | Business Continuity</span>
  </footer>
</div>
</body>
</html>
```